High end personal training flyer design

I want a flyer designed to be delivered to people's houses to interest them in high end (and, therefore, not cheap) personal training services.

Don't want standard pictures of people exercising, before and afters, etc. More something that will appeal to that more affluent market.

Flexible on size of flyer, but please make sure it is a standard size that I can get printed easily. Would like it not to look like a normal flyer you get through the letterbox, so if any particular sizes, shapes, etc are known to do that, then that would be a good start.

Text on flyer to be as follows:

Is this you:

Live in East Cheshire
Male, aged 30-50
A father
Cash rich, time poor
Find handling high pressure at work comfortable
But have a short fuse out of work – with the wife, kids, life in general, etc
Not happy with the way your body looks and feels
Know exactly what you should do to sort that, but struggling to actually do it for various reasons
Turned off by the standard menu of options for addressing that – gyms, slimming clubs, diets, etc

If so, you may be interested in what I do.

Some would call it Personal Training. Some would call it Coaching. I’m not interested in giving what I do labels.

What I am interested in is providing the best possible service (and results) for my clients – whatever that entails.

I work closely with one or two clients at a time to make sure they get exactly what they need.

If you would like to find out more about this, I usually meet for a coffee and a chat. To see if we both think our working together is a good idea.

No squeeze pages, no countdowns, mailing lists or false scarcity.

No plastering this flyer with ‘Before and afters’ – they are ten a penny and my clients don’t want to have pictures of them in their underwear spread around the local area.

Just give me a call and we’ll go from there.

My number is 07912645320.

Tim

Industry/Entity Type

Training

Requirements
Should not have
• Generic before and after or exercise type pictures

```html
<!DOCTYPE html>
<html lang="en">
<head>
<meta charset="utf-8">
<title>Struggling With – Personal Training Flyer</title>
<link rel="stylesheet" href="https://fonts.googleapis.com/css2?family=Oswald:wght@300;400;500&family=Open+Sans:wght@400;600;700&display=swap">
<style>
  :root {
    --backdrop: #9c9c9c;
    --flyer: #060606;
    --white: #ffffff;
    --soft-white: #e6e6e6;
    --muted: #8d8686;
    --tab: #8a8080;
    --tan: #c9a48c;
    --bullet: #dcdcdc;
    --photo-dark: #0b0a0a;
    --photo-mid: #5a4a42;
    --photo-light: #d9d4d0;
  }
  * { box-sizing: border-box; margin: 0; padding: 0; }
  html, body { width: 1200px; height: 1200px; overflow: hidden; }
  body { background: var(--backdrop); position: relative; }

  .flyer {
    position: absolute; left: 150px; top: 35px;
    width: 900px; height: 1130px;
    background: var(--flyer);
    color: var(--white);
    font-family: "Open Sans", Arial, sans-serif;
  }

  /* Headline */
  .headline {
    position: absolute; left: 42px; top: 98px;
    font-family: "Oswald", "Arial Narrow", sans-serif;
    font-weight: 400; font-size: 142px; line-height: 1;
    letter-spacing: -1px; white-space: nowrap;
    transform: scaleX(0.71); transform-origin: left top;
  }
  .with-rule { position: absolute; top: 70px; width: 1.5px; height: 175px; background: var(--soft-white); }
  .with-rule.left { left: 528px; }
  .with-rule.right { left: 580px; }
  .with-tab {
    position: absolute; left: 536px; top: 90px; width: 40px; height: 135px;
    background: var(--tab);
    display: flex; align-items: center; justify-content: center;
  }
  .with-tab span {
    display: block; transform: rotate(-90deg);
    font-family: "Oswald", sans-serif; font-weight: 300; font-size: 24px; letter-spacing: 1px;
    white-space: nowrap;
  }
  .struggle-list { position: absolute; left: 580px; top: 86px; list-style: none; }
  .struggle-list li {
    position: relative; padding-left: 24px; margin-bottom: 9px;
    font-family: "Oswald", sans-serif; font-weight: 400; font-size: 15px; line-height: 1.25;
    white-space: nowrap;
  }
  .struggle-list li::before {
    content: ""; position: absolute; left: 0; top: 9px; width: 12px; height: 1.5px; background: var(--soft-white);
  }
  .struggle-list li::after {
    content: ""; position: absolute; left: 9px; top: 5px; width: 8px; height: 8px; border-radius: 50%; background: var(--bullet);
  }
  .struggle-list .sub { display: block; color: var(--muted); padding-left: 20px; }

  /* Photo area */
  .hero-photo {
    position: absolute; left: 150px; top: 265px; width: 620px; height: 390px;
    background:
      radial-gradient(ellipse 45% 35% at 50% 45%, var(--photo-mid) 0%, rgba(90,74,66,0) 70%),
      linear-gradient(180deg, var(--photo-dark) 0%, #2a2220 25%, var(--photo-light) 52%, #8f8a86 72%, var(--photo-dark) 100%);
    clip-path: polygon(32% 0, 68% 0, 74% 20%, 100% 42%, 100% 70%, 85% 100%, 15% 100%, 0 70%, 0 42%, 26% 20%);
  }

  /* Lower left */
  .question {
    position: absolute; left: 110px; top: 658px;
    font-family: "Oswald", sans-serif; font-weight: 400; font-size: 76px; line-height: 1;
    color: var(--tan); transform: scaleX(0.9); transform-origin: left top; white-space: nowrap;
  }
  .profile { position: absolute; left: 112px; top: 768px; width: 320px; }
  .profile .place { font-weight: 700; font-size: 15px; margin-bottom: 8px; }
  .profile .facts {
    font-family: "Oswald", sans-serif; font-weight: 400; font-size: 19px; margin-bottom: 14px;
    transform: scaleX(0.9); transform-origin: left top; white-space: nowrap;
  }

  .dot-list { list-style: none; }
  .dot-list li {
    position: relative; padding-left: 24px; margin-bottom: 6px;
    font-size: 12.5px; line-height: 1.6; color: var(--soft-white);
  }
  .dot-list li::before {
    content: ""; position: absolute; left: 0; top: 5px; width: 10px; height: 10px; border-radius: 50%; background: var(--bullet);
  }

  /* Lower right */
  .pitch { position: absolute; left: 500px; top: 700px; width: 345px; }
  .pitch h2 {
    font-family: "Oswald", sans-serif; font-weight: 400; font-size: 42px; line-height: 1;
    margin-bottom: 20px; transform: scaleX(0.9); transform-origin: left top; white-space: nowrap;
  }
  .phone-line {
    margin: 4px 0 0 24px;
    font-family: "Oswald", sans-serif; font-weight: 400; font-size: 27px;
    transform: scaleX(0.9); transform-origin: left top; white-space: nowrap;
  }
</style>
</head>
<body>
  <main class="flyer">
    <h1 class="headline">STRUGGLING</h1>
    <div class="with-rule left"></div>
    <div class="with-tab"><span>WITH</span></div>
    <div class="with-rule right"></div>
    <ul class="struggle-list">
      <li>High pressure at work</li>
      <li>Body looks and feels</li>
      <li>Turned off by standard options –<span class="sub">gyms, slimming clubs, diets etc.</span></li>
      <li>Short fuse out of work –<span class="sub">with the wife, kids, life in general</span></li>
    </ul>

    <div class="hero-photo" role="img" aria-label="Photograph of a man in a white shirt leaning over a dark reflective surface, head bowed"></div>

    <p class="question">is this you !</p>
    <section class="profile">
      <p class="place">Live in East Cheshire</p>
      <p class="facts">Male, aged 30-50 &nbsp;|&nbsp; A father &nbsp;|&nbsp; Cash rich, time poor</p>
      <ul class="dot-list">
        <li>Find handling high pressure at work comfortable.</li>
        <li>But have a short fuse out of work – with the wife, kids, life in general, etc.</li>
        <li>Not happy with the way your body looks and feels Know exactly what you should do to sort that, but struggling to actually do it for various reasons.</li>
        <li>Turned off by the standard menu of options for addressing that – gyms, slimming clubs, diets, etc.</li>
      </ul>
    </section>

    <section class="pitch">
      <h2>Rejuvenate your life</h2>
      <ul class="dot-list">
        <li>If so, you may be interested in what I do.</li>
        <li>Some would call it Personal Training. Some would call it Coaching. I’m not interested in giving what I do labels.</li>
        <li>What I am interested in is providing the best possible service (and results) for my clients – whatever that entails.</li>
        <li>I work closely with one or two clients at a time to make sure they get exactly what they need.</li>
        <li>If you would like to find out more about this, I usually meet for a coffee and a chat. To see if we both think our working together is a good idea.</li>
        <li>Just give me (<strong>Tim</strong>) a call</li>
      </ul>
      <p class="phone-line">my number is 07912645320</p>
    </section>
  </main>
</body>
</html>
```